Stationery Design For Specialist London law firm

We have merged two firms of London lawyers to create a new firm with a new name.

The new firms name is KR Holloway. We would like to include the description Solicitors and Advocates in the design.

We need a new design for our headed paper, business cards compliment slips etc.

The image we wish to project is fresh but not gimmicky - reliable and strong but not stuffy.

We have no strong views on font or colour this really is pretty much a blank page.

Our preference is for the name to be at the top of the page

Target Market(s)

Our clients who are individuals rather than corporate and other lawyers

Industry/Entity Type

Law Firm

Requirements
Should not have
• Legal images eg scales of justice etc

Obviously nothing childish or gimmicky

```html
<!DOCTYPE html>
<html lang="en">
<head>
<meta charset="utf-8">
<title>KR Holloway – Stationery</title>
<link rel="stylesheet" href="https://fonts.googleapis.com/css2?family=Cinzel:wght@400;600&family=Arimo:wght@400&display=swap">
<style>
  :root {
    --navy: #0f2a47;
    --navy-mid: #1c3d63;
    --navy-light: #2b5382;
    --ink: #222;
    --grey: #5b5b5b;
    --rule: #9a9a9a;
    --paper: #ffffff;
    --backdrop: #e4e5e7;
  }
  * { box-sizing: border-box; margin: 0; padding: 0; }
  html, body { width: 1200px; height: 900px; overflow: hidden; }
  body { background: var(--backdrop); position: relative; font-family: "Arimo", Arial, sans-serif; }

  .wordmark { font-family: "Cinzel", "Times New Roman", serif; font-weight: 600; color: var(--navy); letter-spacing: 1px; line-height: 1; display: flex; align-items: center; gap: .3em; }
  .wordmark .mark-square { display: inline-block; width: .45em; height: .45em; background: currentColor; }
  .tagline { font-family: "Cinzel", "Times New Roman", serif; color: var(--grey); letter-spacing: .5px; }

  /* Letterhead */
  .letterhead { position: absolute; left: 90px; top: 20px; width: 620px; height: 850px; background: var(--paper); }
  .letterhead .brand { position: absolute; left: 72px; top: 150px; }
  .letterhead .wordmark { font-size: 42px; }
  .letterhead .tagline { font-size: 12px; margin-top: 4px; margin-left: 26px; }
  .letter { position: absolute; left: 82px; top: 238px; width: 460px; color: var(--ink); font-size: 10px; line-height: 17px; }
  .letter .salutation { font-size: 17px; color: var(--grey); margin-bottom: 2px; }
  .letter p { margin-bottom: 17px; }
  .signature { width: 110px; height: 40px; margin-top: 24px; background: linear-gradient(90deg, #cfcfcf, #e6e6e6); border-radius: 3px; }
  .signatory { margin-top: 30px; font-family: "Cinzel", serif; color: var(--navy); font-size: 11px; line-height: 12px; }
  .signatory small { display: block; font-size: 8px; color: var(--grey); }
  .letterhead .contact { position: absolute; right: 30px; top: 742px; text-align: right; font-family: "Cinzel", serif; font-size: 11px; line-height: 15px; color: var(--navy); }
  .letterhead .footer-rule { position: absolute; left: 0; right: 0; bottom: 40px; height: 4px; background: var(--rule); }
  .letterhead .footer-band { position: absolute; left: 0; right: 0; bottom: 0; height: 40px; background: linear-gradient(90deg, var(--navy) 0%, var(--navy-light) 50%, var(--navy) 100%); }

  /* Logo sheet */
  .logo-sheet { position: absolute; left: 726px; top: 0; width: 474px; height: 280px; background: var(--paper); display: flex; flex-direction: column; align-items: center; justify-content: center; }
  .logo-sheet .wordmark { font-size: 54px; margin-top: 70px; }
  .logo-sheet .tagline { font-size: 17px; margin-top: 4px; }

  /* Business card front */
  .card-front { position: absolute; left: 796px; top: 420px; width: 256px; height: 150px; background: var(--paper); overflow: hidden; }
  .card-front .top { height: 78px; position: relative; }
  .card-front .person { position: absolute; left: 12px; top: 58px; font-family: "Cinzel", serif; font-size: 10px; line-height: 10px; color: var(--navy); }
  .card-front .person small { display: block; font-size: 7px; color: var(--grey); }
  .card-front .brand { position: absolute; right: 14px; top: 50px; text-align: right; }
  .card-front .wordmark { font-size: 18px; }
  .card-front .tagline { font-size: 6px; margin-top: 2px; }
  .card-front .bottom { height: 72px; background: linear-gradient(110deg, var(--navy) 0%, var(--navy-light) 60%, var(--navy-mid) 100%); padding: 10px 12px; font-family: "Cinzel", serif; font-size: 7.5px; line-height: 10px; color: #e9eef5; }

  /* Business card back */
  .card-back { position: absolute; left: 808px; top: 612px; width: 266px; height: 156px; background: radial-gradient(circle at 70% 40%, var(--navy-light) 0%, var(--navy) 70%); display: flex; flex-direction: column; align-items: center; justify-content: center; }
  .card-back .wordmark { font-size: 22px; color: #fff; }
  .card-back .tagline { font-size: 8px; color: #c9d3df; margin-top: 3px; }
</style>
</head>
<body>

<section class="letterhead">
  <div class="brand">
    <div class="wordmark"><span class="mark-square"></span>KR Holloway</div>
    <div class="tagline">Solicitors and Advocates</div>
  </div>

  <div class="letter">
    <div class="salutation">Dear client</div>
    <p>We have obtained your name and address from Website, and we are writing to enquire whether you would be willing to establish business relations with us. We have been importers of shoes for many years. At present, We are interested in extending our, range and would appreciate your catalogues and quotations. If your prices are competitive we would expect to transact a significant volume of business. We look forward to your early reply.</p>
    <p>We have obtained your name and address from Website, and we are writing to enquire whether you would be willing to establish business relations with us. We have been importers of shoes for many years. At present, We are interested in extending our, range and would appreciate your catalogues and quotations. If your prices are competitive we would expect to transact a significant volume of business. We look forward to your early reply.</p>
    <p>We have obtained your name and address from Website, and we are writing to enquire whether you would be willing to establish business relations with us. We have been importers of shoes for many years. At present, We are interested in extending our, range and would appreciate your catalogues and quotations. If your prices are competitive we would expect to transact a significant volume of business. We look forward to your early reply.</p>
    <div>Yours Sincerely,</div>
    <div class="signature" role="img" aria-label="Handwritten signature"></div>
    <div class="signatory">Martin Ashby<small>Attorney at Law P.C.</small></div>
  </div>

  <address class="contact">
    A: 48 Carver Lane,<br>
    Suite 9 London EC2A 4PL<br>
    P: +44 20 7946 0123 | F: +44 20 7946 0188<br>
    mail@krholloway.co.uk | www.krholloway.co.uk
  </address>

  <div class="footer-rule"></div>
  <div class="footer-band"></div>
</section>

<section class="logo-sheet">
  <div class="wordmark"><span class="mark-square"></span>KR Holloway</div>
  <div class="tagline">Solicitors and Advocates</div>
</section>

<section class="card-front">
  <div class="top">
    <div class="person">Martin Ashby<small>Attorney at Law P.C.</small></div>
    <div class="brand">
      <div class="wordmark"><span class="mark-square"></span>KR Holloway</div>
      <div class="tagline">Solicitors and Advocates</div>
    </div>
  </div>
  <address class="bottom">
    A: 48 Carver Lane,<br>
    Suite 9 London EC2A 4PL<br>
    P: +44 20 7946 0123 | F: +44 20 7946 0188<br>
    mail@krholloway.co.uk | www.krholloway.co.uk
  </address>
</section>

<section class="card-back">
  <div class="wordmark"><span class="mark-square"></span>KR Holloway</div>
  <div class="tagline">Solicitors and Advocates</div>
</section>

</body>
</html>
```